Pemberton Dialworks Business Card Design

Double Sided Business Card Design for a Locksmith company specializing in Safecracking, safe & vault service.

```html
<!DOCTYPE html>
<html lang="en">
<head>
<meta charset="utf-8">
<title>Pemberton Dialworks — Business Card</title>
<link rel="stylesheet" href="https://fonts.googleapis.com/css2?family=Montserrat:wght@400;600;800&display=swap">
<style>
  :root {
    --stage: #000000;
    --card: #ffffff;
    --green: #3b7d3c;
    --ink: #222222;
    --muted: #555555;
    --skyline: #dddcdc;
    --skyline-fade: #f4f4f4;
    --label: #ffffff;
  }
  * { box-sizing: border-box; margin: 0; padding: 0; }
  html, body { width: 903px; height: 1200px; overflow: hidden; background: var(--stage); }
  body { font-family: "Montserrat", sans-serif; position: relative; }

  .card {
    position: absolute; left: 100px; width: 560px; height: 336px;
    background: var(--card); overflow: hidden;
  }
  .card--back { top: 190px; }
  .card--front { top: 640px; }

  .side-label {
    position: absolute; left: 720px; color: var(--label);
    font-family: "Montserrat", sans-serif; font-weight: 400; font-size: 36px;
  }
  .side-label--back { top: 335px; }
  .side-label--front { top: 785px; }

  .back-arc { position: absolute; inset: 0; }

  .brand {
    position: absolute; display: flex; align-items: center;
    color: var(--green); font-weight: 800; line-height: 1.02;
  }
  .brand__mark { border-radius: 50%; background: var(--green); flex: none; }
  .brand--back { left: 320px; top: 78px; font-size: 22px; gap: 14px; }
  .brand--back .brand__mark { width: 40px; height: 40px; }
  .brand--front { left: 226px; top: 140px; font-size: 26px; gap: 20px; }
  .brand--front .brand__mark { width: 58px; height: 58px; }

  .holder { position: absolute; left: 32px; top: 118px; color: #fff; }
  .holder__name { font-weight: 600; font-size: 27px; letter-spacing: 0.2px; }
  .holder__role { margin-top: 12px; margin-left: 5px; font-size: 15px; letter-spacing: 3px; }

  .contacts { position: absolute; left: 38px; top: 222px; list-style: none; color: #fff; font-size: 14px; }
  .contacts li { display: flex; align-items: center; gap: 20px; height: 27px; }
  .contacts .bullet {
    width: 17px; height: 17px; border-radius: 50%;
    background: #fff; border: 4px solid var(--ink); flex: none;
  }

  .address { position: absolute; left: 344px; top: 228px; color: var(--muted); font-size: 12.5px; line-height: 18px; }
  .address-dot {
    position: absolute; left: 315px; top: 227px; width: 17px; height: 17px;
    border-radius: 50%; background: #fff; border: 3px solid var(--green);
  }

  .skyline {
    position: absolute; left: 0; top: 157px; width: 242px; height: 179px;
    background: linear-gradient(160deg, var(--skyline-fade) 0%, var(--skyline) 55%, var(--skyline) 100%);
  }
</style>
</head>
<body>
  <section class="card card--back" aria-label="Card back">
    <svg class="back-arc" width="560" height="336" viewBox="0 0 560 336" aria-hidden="true">
      <circle cx="62" cy="303" r="273" fill="var(--green)"/>
    </svg>

    <div class="brand brand--back">
      <span class="brand__mark"></span>
      <span class="brand__name">Pemberton<br>Dialworks</span>
    </div>

    <div class="holder">
      <p class="holder__name">Your Name</p>
      <p class="holder__role">DESIGNATION</p>
    </div>

    <ul class="contacts">
      <li><span class="bullet"></span>+91 0123456789</li>
      <li><span class="bullet"></span>lorem.ipsum@lorem.com</li>
      <li><span class="bullet"></span>www.loremipsum.com</li>
    </ul>

    <span class="address-dot"></span>
    <p class="address">Lorem Ipsum, Dummy text<br>Lorem Ipsum, Dummy text<br>ipsum industry 123456</p>
  </section>
  <p class="side-label side-label--back">Back</p>

  <section class="card card--front" aria-label="Card front">
    <div class="skyline" role="img" aria-label="Faint grey city skyline silhouette"></div>
    <div class="brand brand--front">
      <span class="brand__mark"></span>
      <span class="brand__name">Pemberton<br>Dialworks</span>
    </div>
  </section>
  <p class="side-label side-label--front">Front</p>
</body>
</html>
```